Poster for teenagers

Bright, trendy, modern and young fonts - a variety of fonts, plus arrows and clip art (no photos) for an A3 size poster to be hung in study halls of schools. There are six dot points. I think each point should be in some kind of box or circle.

Here are a few ideas of the kind of thing I mean.
http://www.tarnwick.example.au/Page/Images/youth_Advisory_Group_Poster_(1).jpg

http://www.holmbrae.example.ie/sites/default/files/Youth-Panel-Poster-1-Web.jpg

http://www.quillmarsh.example.au/images/librariesprovider4/Misc-illustrations/140335-qml-youth-superheros-heroup-highres.jpg?sfvrsn=0

https://rvkointernational.files.examplepress.com/2013/04/544477_432153653542694_970534114_n.jpg

Also my logo should be on it some where . I've attached a my logo.

Here is the text:
How to get organised and motivated this year.
1. Write stuff down
Write down things you need to do and when you plan to do them. Use digital calendars, to do apps and email lists – or pen and paper. Even if you are sure you will remember – get it out of your head and onto paper/your phone/laptop. You are more likely to get it done and feel less stressed.
2. Set up habits
If you do things in the same way, at the same time or after the same thing – then after a few weeks, it becomes much easier to get those things done. Set up a particular time, or place to do study tasks – or link them with another daily task. EG: art homework every Tuesday. Violin practice after breakfast.
3. Focus!
For 15-30 minutes at a time - totally focus on homework. Put your phone away, log out of chatterbox, close down other programs and really concentrate. Then have a break, send a text or whatever – and then go back to focussed study. Fifteen minutes of concentrated study gets more achieved than an hour of study switching back and forth between homework and other activities.
4. Just do something
No motivation? Just take a “bite”. Set a timer and just do 5 minutes. Or 15. Or read just the first two pages. Or the first problem on the worksheet. Something is better than nothing – and sometimes once you start, it’s easier to keep going.
5. Use rewards and consequences
Reward yourself when you do a hard task and use consequences when you don’t. Use food, fun activities, gaming and social time to motivate yourself – you get it when you do tasks, you don’t when you don’t. EG 15 minutes of vidloop when I finish this page. Tell other people your plans and you are more likely to stick to them.
6. Imagine the future
When you really can’t be find any motivation to do the things you need to do – take 30 seconds to think about what will happen in a week, month and year if you get on with it. What will happen then and how will that feel. And imagine what will happen in a week, month and year if you DON’T do those things – and how will that feel.

Good luck !
For free articles and one to one help with study skills, increasing motivation, coping with stress or tough times in senior school, go to brightpathlearning.example.au
Brightpath Learning Psychology and Education

```html
<!DOCTYPE html>
<html lang="en">
<head>
<meta charset="utf-8">
<title>How to get organised and motivated this year</title>
<link rel="stylesheet" href="https://fonts.googleapis.com/css2?family=Bebas+Neue&family=Oswald:wght@400;500&family=Prata&family=Roboto+Condensed:wght@400&display=swap">
<style>
  :root {
    --panel-light: #229a74;
    --panel-dark: #176a58;
    --logo-paper: #e3e7a8;
    --logo-fold: #b9bf98;
    --ink-dark: #1f6a52;
    --ring: #c98fb4;
    --c-write: rgba(178, 222, 170, 0.92);
    --c-habits: rgba(222, 190, 208, 0.92);
    --c-focus: rgba(176, 190, 235, 0.92);
    --c-just: rgba(165, 228, 218, 0.92);
    --c-rewards: rgba(172, 230, 164, 0.92);
    --c-future: rgba(200, 232, 176, 0.94);
    --t-write: #e6f2b4;
    --t-habits: #fff6ea;
    --t-focus: #e0e6ff;
    --t-just: #fbfbf3;
    --t-rewards: #ecf4a6;
    --t-future: #f8f4c4;
    --white: #ffffff;
  }
  * { margin: 0; padding: 0; box-sizing: border-box; }
  html, body { width: 856px; height: 1200px; overflow: hidden; background: var(--white); }
  .poster {
    position: relative; width: 856px; height: 1200px; background: var(--white);
  }
  .panel {
    position: absolute; left: 0; top: 0; width: 843px; height: 1190px;
    background: radial-gradient(ellipse 70% 55% at 58% 48%, var(--panel-light), var(--panel-dark));
  }
  .logo-tag {
    position: absolute; left: 229px; top: 0; width: 384px; height: 126px;
    background: var(--logo-paper);
    clip-path: polygon(0 0, 100% 0, 100% 76%, 88% 100%, 0 100%);
    display: flex; align-items: center; justify-content: center;
    font-family: "Oswald", sans-serif; font-weight: 400; font-size: 60px; color: #000;
    letter-spacing: 1px; padding-bottom: 6px;
  }
  .logo-fold {
    position: absolute; left: 565px; top: 97px; width: 48px; height: 29px;
    background: var(--logo-fold);
    clip-path: polygon(100% 0, 0 100%, 10% 10%);
  }
  .shapes { position: absolute; left: 0; top: 0; }
  .badge {
    position: absolute; display: flex; flex-direction: column; align-items: center; justify-content: center;
    font-family: "Bebas Neue", sans-serif; color: var(--ink-dark); text-align: center; line-height: 0.98;
  }
  .tip {
    position: absolute; font-family: "Prata", serif; font-size: 17.2px; line-height: 25px;
  }
  .tip--write { left: 214px; top: 151px; width: 615px; color: var(--t-write); }
  .tip--habits { left: 244px; top: 306px; width: 590px; color: var(--t-habits); }
  .tip--focus { left: 182px; top: 445px; width: 660px; color: var(--t-focus); }
  .tip--just { left: 200px; top: 607px; width: 625px; color: var(--t-just); }
  .tip--rewards { left: 218px; top: 721px; width: 625px; color: var(--t-rewards); }
  .tip--future { left: 237px; top: 878px; width: 585px; color: var(--t-future); }
  .good-luck {
    position: absolute; left: 0; width: 843px; top: 1036px; text-align: center;
    font-family: "Bebas Neue", sans-serif; font-size: 60px; color: var(--white); line-height: 1;
  }
  .footer-note {
    position: absolute; left: 0; width: 843px; top: 1103px; text-align: center;
    font-family: "Roboto Condensed", sans-serif; font-size: 13px; line-height: 20px; color: var(--white);
  }
  .footer-note .site { font-size: 14px; }
  .credit {
    position: absolute; left: 0; width: 843px; top: 1158px; text-align: center;
    font-family: "Roboto Condensed", sans-serif; font-size: 11px; color: var(--white);
  }
</style>
</head>
<body>
<div class="poster">
  <div class="panel"></div>

  <svg class="shapes" width="856" height="1200" viewBox="0 0 856 1200" aria-hidden="true">
    <g stroke="rgba(255,255,255,0.35)" stroke-width="1">
      <line x1="68" y1="0" x2="68" y2="140"/>
      <line x1="100" y1="0" x2="100" y2="138"/>
      <line x1="130" y1="0" x2="130" y2="284"/>
      <line x1="148" y1="0" x2="148" y2="284"/>
      <line x1="38" y1="330" x2="38" y2="440"/>
      <line x1="60" y1="580" x2="60" y2="570"/>
    </g>
    <g>
      <circle cx="88" cy="218" r="80" fill="var(--c-write)"/>
      <circle cx="88" cy="218" r="70" fill="none" stroke="var(--ring)" stroke-width="1.6"/>
      <circle cx="145" cy="362" r="79" fill="var(--c-habits)"/>
      <circle cx="145" cy="362" r="69" fill="none" stroke="var(--ring)" stroke-width="1.6"/>
      <circle cx="79" cy="507" r="77" fill="var(--c-focus)"/>
      <circle cx="79" cy="507" r="67" fill="none" stroke="var(--ring)" stroke-width="1.6"/>
      <circle cx="102" cy="648" r="88" fill="var(--c-just)"/>
      <circle cx="102" cy="648" r="77" fill="none" stroke="var(--ring)" stroke-width="1.6"/>
      <circle cx="108" cy="798" r="81" fill="var(--c-rewards)"/>
      <circle cx="108" cy="798" r="71" fill="none" stroke="var(--ring)" stroke-width="1.6"/>
      <circle cx="117" cy="955" r="105" fill="var(--c-future)"/>
      <circle cx="117" cy="955" r="93" fill="none" stroke="var(--ring)" stroke-width="1.6"/>
    </g>
  </svg>

  <div class="logo-tag">YOUR LOGO</div>
  <div class="logo-fold"></div>

  <div class="badge" style="left:18px; top:148px; width:140px; height:140px; font-size:38px; line-height:1.22;">WRITE<br>STUFF<br>DOWN</div>
  <div class="badge" style="left:75px; top:292px; width:140px; height:140px; font-size:50px; line-height:0.9;">SET UP<br>HABITS</div>
  <div class="badge" style="left:9px; top:437px; width:140px; height:140px; font-size:54px;">FOCUS!</div>
  <div class="badge" style="left:27px; top:573px; width:150px; height:150px; font-size:36px; line-height:1.3;">JUST DO<br>SOMETHING</div>
  <div class="badge" style="left:38px; top:728px; width:140px; height:140px;">
    <span style="font-size:26px;">USE</span>
    <span style="font-size:40px; line-height:0.85;">REWARDS</span>
    <span style="font-size:26px; line-height:0.9;">AND</span>
    <span style="font-size:24px;">CONSEQUENCES</span>
  </div>
  <div class="badge" style="left:27px; top:865px; width:180px; height:180px;">
    <span style="font-size:56px; line-height:0.92;">IMAGINE</span>
    <span style="font-size:40px; line-height:0.92;">THE</span>
    <span style="font-size:60px; line-height:0.92;">FUTURE</span>
  </div>

  <p class="tip tip--write">Write down things you need to do and when you plan to do them. Use digital calendars, to do apps and email lists – or pen and paper. Even if you are sure you will remember – get it out of your head and onto paper/your phone/laptop. You are more likely to get it done and feel less stressed.</p>
  <p class="tip tip--habits">If you do things in the same way, at the same time or after the same thing – then after a few weeks, it becomes much easier to get those things done. Set up a particular time, or place to do study tasks – or link them with another daily task. EG: art homework every Tuesday. Violin practice after breakfast.</p>
  <p class="tip tip--focus">For 15-30 minutes at a time - totally focus on homework. Put your phone away, log out of chatterbox, close down other programs and really concentrate. Then have a break, send a text or whatever – and then go back to focussed study. Fifteen minutes of concentrated study gets more achieved than an hour of study switching back and forth between homework and other activities.</p>
  <p class="tip tip--just">No motivation? Just take a “bite”. Set a timer and just do 5 minutes. Or 15. Or read just the first two pages. Or the first problem on the worksheet. Something is better than nothing – and sometimes once you start, it’s easier to keep going.</p>
  <p class="tip tip--rewards">Reward yourself when you do a hard task and use consequences when you don’t. Use food, fun activities, gaming and social time to motivate yourself – you get it when you do tasks, you don’t when you don’t. EG 15 minutes of vidloop when I finish this page. Tell other people your plans and you are more likely to stick to them.</p>
  <p class="tip tip--future">When you really can’t be find any motivation to do the things you need to do – take 30 seconds to think about what will happen in a week, month and year if you get on with it. What will happen then and how will that feel. And imagine what will happen in a week, month and year if you DON’T do those things – and how will that feel.</p>

  <div class="good-luck">GOOD LUCK</div>
  <p class="footer-note">For free articles and one to one help with study skills, increasing motivation, coping with stress or tough times in senior school, go to<br><span class="site">brightpathlearning.example.au</span></p>
  <p class="credit">Brightpath Learning Psychology and Education</p>
</div>
</body>
</html>
```